Hop Grower Producer Card

A wisconsin based grower of high quality mid westrn grown Hops with the concept of growing and processing Hops into pellet form for sale to brewers of beer large and small .varieties are grown are Cascade ,Chinook and Centennial

Target Market(s)

Brew masters at micro brews and large breweries

Industry/Entity Type

Processing

Font styles to use
Decorative
Script

Requirements
Must have
• i would like the Hop varieties listed on the back of the card , with the statement Grower of High Quality Wisconsin Hops and the web site address
Nice to have
• german style font for the name Volmer's Bine Lodge

```html
<!DOCTYPE html>
<html lang="en">
<head>
<meta charset="utf-8">
<title>Volmer's Bine Lodge – Hop Varieties Card</title>
<link rel="stylesheet" href="https://fonts.googleapis.com/css2?family=UnifrakturMaguntia&family=Noto+Serif:wght@400&display=swap">
<style>
  :root {
    --card-bg: #ebfa8a;
    --vine-tone: #dcee78;
    --vine-soft: #e3f482;
    --ink: #1d2a08;
  }
  html, body {
    margin: 0;
    padding: 0;
    width: 1200px;
    height: 702px;
    overflow: hidden;
    background: var(--card-bg);
  }
  .card {
    position: relative;
    width: 1200px;
    height: 702px;
    background: var(--card-bg);
    overflow: hidden;
    color: var(--ink);
  }
  .vine-backdrop {
    position: absolute;
    inset: 0;
    background:
      radial-gradient(ellipse at 20% 30%, var(--vine-tone) 0%, transparent 45%),
      radial-gradient(ellipse at 85% 25%, var(--vine-tone) 0%, transparent 40%),
      radial-gradient(ellipse at 70% 80%, var(--vine-tone) 0%, transparent 45%),
      radial-gradient(ellipse at 15% 85%, var(--vine-soft) 0%, transparent 40%),
      var(--card-bg);
  }
  .brand-name {
    position: absolute;
    top: 88px;
    left: 0;
    width: 100%;
    margin: 0;
    text-align: center;
    font-family: "UnifrakturMaguntia", serif;
    font-weight: 400;
    font-size: 60px;
    letter-spacing: 6px;
    line-height: 1;
  }
  .tagline {
    position: absolute;
    top: 184px;
    left: 0;
    width: 100%;
    margin: 0;
    text-align: center;
    font-family: "Noto Serif", serif;
    font-size: 28px;
    letter-spacing: 0.5px;
    line-height: 1;
  }
  .varieties {
    position: absolute;
    top: 340px;
    left: 0;
    width: 100%;
    margin: 0;
    text-align: center;
    font-family: "UnifrakturMaguntia", serif;
    font-size: 62px;
    letter-spacing: 5px;
    word-spacing: 18px;
    line-height: 1;
  }
  .web-address {
    position: absolute;
    top: 604px;
    left: 0;
    width: 100%;
    margin: 0;
    text-align: center;
    font-family: "Noto Serif", serif;
    font-size: 28px;
    letter-spacing: 2px;
    line-height: 1;
  }
</style>
</head>
<body>
  <main class="card">
    <div class="vine-backdrop" role="img" aria-label="Faint pattern of climbing hop vines and leaves across the card"></div>
    <h1 class="brand-name">Volmer's Bine Lodge</h1>
    <p class="tagline">Grower of High Quality Wisconsin Hops</p>
    <p class="varieties">Cascade Chinook Centennial</p>
    <p class="web-address">www.binelodge47.com</p>
  </main>
</body>
</html>
```